Brand new letterhead, business card, email signature etc.

We are a financial company in London, UK. Our website is www.quorvane.com. We're wanting a complete remodel of the company colours, letter head, business cards, email signatures, etc. Looking to keep the same font for the company name. I have upload a colour palette that we want to work with. We're looking for company letterhead for outgoing letters/ correspondence, letterhead for internal documentation, email signatures, e-letters. etc. Ultimately we will redesign the entire website also. It is important that our clients get a strong, secure, warm, trustworthy, solid feeling and first impression.
Updates

Designs look the same

Target Market(s)

Institutional investors, (ultra) high net worth individuals

Industry/Entity Type

Finance, Invesments banking.

Font styles to use
Other font styles liked:
• Current font is "Champagne & Limousines"

Requirements
Must have
• Must use the colours provided on the PDF uploaded to the portal. The purple = main colour. The red = accent colour.
Nice to have
• Nice to use same font as now for the company name "Marlowin". Font is "Champagne & Limousines". Nice to have some reference to the old logo flower, but only subtle.
Should not have
• Do not use the colour red from our website. Use the colours provided on the colour palette PDF that I uploaded in the portal.

```html
<!DOCTYPE html>
<html lang="en">
<head>
<meta charset="utf-8">
<title>Marlowin Business Card</title>
<link rel="stylesheet" href="https://fonts.googleapis.com/css2?family=Josefin+Sans:wght@300&family=Open+Sans:wght@400;600&display=swap">
<style>
  :root {
    --bg: #7f9abd;
    --card: #ffffff;
    --red: #e2412f;
    --plum: #2e1823;
    --ink: #2b2b2b;
    --rule: #555555;
  }
  * { margin: 0; padding: 0; box-sizing: border-box; }
  html, body { width: 1200px; height: 876px; overflow: hidden; }
  body {
    background: var(--bg);
    font-family: "Open Sans", sans-serif;
    color: var(--ink);
    position: relative;
  }
  .card {
    position: absolute;
    top: 290px;
    width: 520px;
    height: 297px;
    background: var(--card);
    overflow: hidden;
  }
  .card--front { left: 60px; }
  .card--back { left: 620px; }

  /* Front */
  .corner-block {
    position: absolute; left: 0; top: 0;
    width: 44px; height: 26px;
    background: var(--plum);
  }
  .brand {
    position: absolute; left: 54px; top: 30px;
    display: flex; align-items: center; gap: 8px;
  }
  .brand__square {
    width: 26px; height: 26px;
    border: 1px solid var(--ink);
  }
  .brand__name {
    font-family: "Josefin Sans", sans-serif;
    font-weight: 300;
    font-size: 15px;
    letter-spacing: 3px;
    line-height: 1;
    color: var(--ink);
    text-transform: uppercase;
  }
  .accent-band {
    position: absolute; left: 250px; top: 46px;
    width: 270px; height: 24px;
    background: var(--red);
  }
  .person {
    position: absolute; left: 58px; top: 100px;
  }
  .person__name {
    font-size: 24px; font-weight: 400; letter-spacing: 0.5px;
    text-transform: uppercase; color: var(--ink);
  }
  .person__name strong { font-weight: 600; }
  .person__title {
    font-size: 11px; letter-spacing: 2.5px; color: var(--red);
    margin-top: 2px;
  }
  .divider {
    position: absolute; left: 40px; top: 168px;
    width: 480px; height: 1px;
    background: var(--rule);
  }
  .contacts {
    position: absolute; left: 40px; top: 180px;
    list-style: none;
    font-size: 10.5px; font-weight: 600; line-height: 1.55;
  }
  .contacts li { display: flex; align-items: flex-start; gap: 8px; }
  .contacts svg { flex: none; margin-top: 2px; }

  /* Back */
  .back-band-red {
    position: absolute; left: 0; top: 40px;
    width: 160px; height: 30px;
    background: var(--red);
  }
  .back-band-plum {
    position: absolute; right: 0; top: 160px;
    width: 170px; height: 34px;
    background: linear-gradient(90deg, #3f2230, var(--plum));
  }
  .back-mark {
    position: absolute; left: 185px; top: 50px;
    width: 150px; height: 150px;
    border: 1px solid var(--ink);
    display: flex; align-items: center; justify-content: center;
  }
  .back-mark__name {
    font-family: "Josefin Sans", sans-serif;
    font-weight: 300;
    font-size: 14px;
    letter-spacing: 3px;
    line-height: 1;
    text-transform: uppercase;
    color: var(--ink);
  }
  .web {
    position: absolute; left: 152px; top: 214px;
    display: flex; align-items: center; gap: 8px;
    font-size: 12px; color: var(--ink);
  }
</style>
</head>
<body>
  <section class="card card--front" aria-label="Business card front">
    <div class="corner-block"></div>
    <div class="brand">
      <div class="brand__square"></div>
      <span class="brand__name">Marlowin</span>
    </div>
    <div class="accent-band"></div>
    <div class="person">
      <h1 class="person__name"><strong>Dana</strong> Whitfield</h1>
      <p class="person__title">Marketing Manager</p>
    </div>
    <div class="divider"></div>
    <ul class="contacts">
      <li>
        <svg width="11" height="11" viewBox="0 0 24 24" fill="var(--red)"><path d="M6.6 10.8a15 15 0 0 0 6.6 6.6l2.2-2.2c.3-.3.7-.4 1-.2 1.1.4 2.3.6 3.6.6.6 0 1 .4 1 1V20c0 .6-.4 1-1 1A17 17 0 0 1 3 4c0-.6.4-1 1-1h3.5c.6 0 1 .4 1 1 0 1.3.2 2.5.6 3.6.1.3 0 .7-.2 1z"/></svg>
        <span>+44 20 7946 0381</span>
      </li>
      <li>
        <svg width="11" height="11" viewBox="0 0 24 24" fill="var(--red)"><path d="M2 12 22 3l-6 19-4-8z"/></svg>
        <span>info@marlowin.com</span>
      </li>
      <li>
        <svg width="11" height="12" viewBox="0 0 24 26" fill="var(--red)"><path d="M12 0a9 9 0 0 0-9 9c0 7 9 17 9 17s9-10 9-17a9 9 0 0 0-9-9zm0 12.5A3.5 3.5 0 1 1 12 5.5a3.5 3.5 0 0 1 0 7z"/></svg>
        <span>Marlowin Group Limited, 4th Floor,<br>18 Aldgate Row, London, EC3N 2LB</span>
      </li>
    </ul>
  </section>

  <section class="card card--back" aria-label="Business card back">
    <div class="back-band-red"></div>
    <div class="back-mark">
      <span class="back-mark__name">Marlowin</span>
    </div>
    <div class="back-band-plum"></div>
    <div class="web">
      <svg width="13" height="13" viewBox="0 0 24 24" fill="none" stroke="var(--red)" stroke-width="2.4"><circle cx="12" cy="12" r="10"/><path d="M2 12h20M12 2c3 3 3 17 0 20M12 2c-3 3-3 17 0 20"/></svg>
      <span>www.quorvane.com</span>
    </div>
  </section>
</body>
</html>
```